Letterhead Design Project

Letterhead for a Consultant Cardiologist in Adelaide Australia. Should be very classy, mature and imposing. I would prefer colours that portray confidence, gentleness and serenity.

The PDF attached is for you to see the details that will be on the letterhead and not the design which is extremely poor!

Target Market(s)

Health professionals especially medical doctors

Industry/Entity Type

Consultant

```html
<!DOCTYPE html>
<html lang="en">
<head>
<meta charset="utf-8">
<title>Dr Adebayo T. Nwankwo – Letterhead</title>
<link href="https://fonts.googleapis.com/css2?family=Tinos:wght@700&family=Open+Sans:wght@400;700&family=Questrial&display=swap" rel="stylesheet">
<style>
  :root{
    --red:#c8191f;
    --red-dark:#a81217;
    --grey-light:#f2f2f3;
    --grey-mid:#c9cacc;
    --grey-text:#9a9a9a;
    --ink:#111111;
    --ink-soft:#3c3c3c;
    --paper:#ffffff;
  }
  *{margin:0;padding:0;box-sizing:border-box}
  html,body{width:848px;height:1200px;overflow:hidden;background:var(--paper)}
  .letterhead{position:relative;width:848px;height:1200px;background:var(--paper);overflow:hidden}

  .header-band{position:absolute;left:0;top:0;width:848px;height:158px;
    background:linear-gradient(90deg,var(--grey-mid) 0%,var(--grey-light) 45%,#fafafa 60%,var(--grey-mid) 100%)}
  .header-rules{position:absolute;left:0;top:150px;width:848px;height:40px}

  .brand{position:absolute;left:240px;top:30px}
  .brand-mark{position:absolute;left:0;top:30px;width:42px;height:42px;border-radius:50%;background:var(--red)}
  .doctor-name{position:absolute;left:112px;top:20px;white-space:nowrap;
    font-family:'Tinos',serif;font-weight:700;font-size:21px;color:var(--ink)}
  .credentials{position:absolute;left:112px;top:54px;white-space:nowrap;
    font-family:'Open Sans',sans-serif;font-size:13px;color:var(--ink-soft);letter-spacing:.3px}
  .specialty{position:absolute;left:112px;top:73px;white-space:nowrap;
    font-family:'Open Sans',sans-serif;font-weight:700;font-size:15px;color:var(--red)}

  .footer-details{position:absolute;top:1070px;font-style:normal;font-family:'Questrial',sans-serif;font-size:12.5px;line-height:15.4px;color:var(--grey-text);white-space:nowrap}
  .footer-details .label{color:var(--red-dark)}
  .footer-details .dark{color:var(--ink-soft)}
  .col-consulting{left:30px;width:170px}
  .col-riverside{left:210px;width:350px}
  .col-bayside{left:568px;width:170px}
  .email-line{position:relative}
  .provider-inline{position:absolute;left:185px;top:0;color:var(--ink-soft)}

  .footer-bands{position:absolute;left:0;top:1166px;width:848px;height:34px}
</style>
</head>
<body>
<main class="letterhead">
  <div class="header-band" role="img" aria-label="Soft grey band with a faint repeating heart pattern"></div>
  <svg class="header-rules" viewBox="0 0 848 40" aria-hidden="true">
    <rect x="0" y="0" width="848" height="8" fill="#7d7f82"/>
    <rect x="0" y="8" width="848" height="5" fill="var(--red)"/>
    <rect x="0" y="13" width="848" height="3" fill="#6f7174"/>
    <polygon points="648,16 848,16 848,35 668,35" fill="#b5b6b8"/>
  </svg>

  <header class="brand">
    <span class="brand-mark"></span>
    <h1 class="doctor-name">Dr Adebayo. T. Nwankwo</h1>
    <p class="credentials">M.B.B.S, F.M.C.P, F.R.A.C.P</p>
    <p class="specialty">Cardiologist</p>
  </header>

  <footer>
    <address class="footer-details col-consulting">
      <div class="label">Consulting</div>
      <div class="label">The Avon Specialist Centre</div>
      <div>18 Linden Road</div>
      <div>Linden Park SA 5065</div>
      <div class="dark">T: 8123 4567</div>
      <div class="dark">F: 8123 4568</div>
    </address>
    <address class="footer-details col-riverside">
      <div class="label">Provider No: 512884AB</div>
      <div class="label">Riverside Cardiology</div>
      <div>&amp; Specialist Clinic, Hillcrest Central Districts, Private Hospital</div>
      <div>40-52 Marlow Road, Seaford Vale SA 5160</div>
      <div class="dark">T: 8130 2200 &nbsp;&nbsp;F: 8130 2211</div>
      <div class="email-line">E: cardiology@rvsc.example<span class="provider-inline">Provider No: 512884CD</span></div>
    </address>
    <address class="footer-details col-bayside">
      <div class="label">Bayside Regional Hospital</div>
      <div>9 Jetty Road</div>
      <div>Bayside 5710</div>
      <div class="dark">T: 8140 3300</div>
      <div class="dark">F: 8123 4568</div>
      <div class="dark">Provider No: 512884EF</div>
    </address>
    <svg class="footer-bands" viewBox="0 0 848 34" aria-hidden="true">
      <polygon points="0,0 706,0 722,17 0,17" fill="#a9aaac"/>
      <rect x="0" y="17" width="848" height="17" fill="var(--red)"/>
    </svg>
  </footer>
</main>
</body>
</html>
```